Corwin Crest Homes Needs Business Card Design

Looking for a unique modern business card to fit my new Logo.
Name: Marcus Corwin
Company: Corwin Crest Homes, LLC
Tag Line: Always Built Better
Email: corwincresthomes@mailnest.example
Phone: (555) 017-2846
Website: www.corwincresthomes.example
License: CORWICH462KX

```html
<!DOCTYPE html>
<html lang="en">
<head>
<meta charset="utf-8">
<title>Corwin Crest Homes – Business Card</title>
<link href="https://fonts.googleapis.com/css2?family=Montserrat:wght@400;500;700;800&display=swap" rel="stylesheet">
<style>
  :root {
    --ink: #0b0b0b;
    --paper: #ffffff;
    --brand-blue: #3a95d1;
    --stage: #e6e7e9;
    --rule: #1a1a1a;
    --text: #222222;
  }
  html, body {
    margin: 0;
    padding: 0;
    width: 1200px;
    height: 998px;
    overflow: hidden;
    background: var(--stage);
    font-family: "Montserrat", sans-serif;
  }
  .canvas {
    position: relative;
    width: 1200px;
    height: 998px;
  }
  .card {
    position: absolute;
    left: 240px;
    width: 720px;
    height: 412px;
    overflow: hidden;
    box-shadow: 0 6px 18px rgba(0,0,0,0.18);
  }
  .card--front { top: 60px; background: var(--ink); }
  .card--back  { top: 526px; background: var(--paper); }

  /* Front */
  .front-brand {
    position: absolute;
    left: 0; right: 0;
    top: 150px;
    display: flex;
    justify-content: center;
    align-items: center;
    gap: 16px;
  }
  .brand-square {
    width: 34px;
    height: 34px;
    background: var(--brand-blue);
    flex: none;
  }
  .brand-name {
    font-weight: 800;
    font-size: 40px;
    letter-spacing: 0.5px;
    text-transform: uppercase;
    white-space: nowrap;
  }
  .front-brand .brand-name { color: var(--paper); }
  .tagline {
    position: absolute;
    left: 0; right: 0;
    top: 290px;
    margin: 0;
    text-align: center;
    color: var(--paper);
    font-weight: 400;
    font-size: 22px;
    letter-spacing: 1px;
  }

  /* Back */
  .accent-bar {
    position: absolute;
    right: 0;
    top: 30px;
    width: 16px;
    height: 68px;
    background: var(--brand-blue);
  }
  .person {
    position: absolute;
    right: 50px;
    top: 34px;
    text-align: right;
  }
  .person-name {
    color: var(--brand-blue);
    font-weight: 800;
    font-size: 34px;
    line-height: 1.1;
  }
  .person-title {
    color: var(--text);
    font-weight: 500;
    font-size: 18px;
    margin-top: 2px;
  }
  .back-brand {
    position: absolute;
    left: 56px;
    top: 150px;
    display: flex;
    align-items: center;
    gap: 14px;
  }
  .back-brand .brand-name { color: var(--ink); font-size: 32px; }
  .back-brand .brand-square { width: 28px; height: 28px; }

  .divider {
    position: absolute;
    left: 56px;
    right: 46px;
    top: 214px;
    height: 1.5px;
    background: var(--rule);
  }
  .company {
    position: absolute;
    right: 46px;
    top: 226px;
    text-align: right;
  }
  .company-name {
    font-weight: 700;
    font-size: 19px;
    color: var(--ink);
  }
  .contact-line {
    display: flex;
    align-items: center;
    gap: 8px;
    font-weight: 400;
    font-size: 18px;
    line-height: 24px;
    color: var(--text);
    margin-top: 4px;
    white-space: nowrap;
  }
  .company .contact-line { justify-content: flex-end; }
  .icon { width: 18px; height: 18px; flex: none; }

  .contacts {
    position: absolute;
    left: 56px;
    top: 284px;
  }
  .contacts .contact-line { margin-top: 4px; }

  .footer-shapes {
    position: absolute;
    left: 0;
    top: 0;
    width: 720px;
    height: 412px;
  }
  .license {
    position: absolute;
    right: 28px;
    bottom: 16px;
    color: var(--brand-blue);
    font-weight: 700;
    font-size: 20px;
    line-height: 24px;
    white-space: nowrap;
  }
</style>
</head>
<body>
<main class="canvas">

  <section class="card card--front" aria-label="Card front">
    <div class="front-brand">
      <span class="brand-square"></span>
      <span class="brand-name">Corwin Crest Homes</span>
    </div>
    <p class="tagline">ALWAYS BUILT BETTER</p>
  </section>

  <section class="card card--back" aria-label="Card back">
    <svg class="footer-shapes" viewBox="0 0 720 412" aria-hidden="true">
      <polygon points="0,388 346,388 338,404 0,404" fill="var(--brand-blue)"/>
      <polygon points="356,412 376,372 720,346 720,412" fill="var(--ink)"/>
    </svg>

    <div class="accent-bar"></div>
    <div class="person">
      <div class="person-name">Marcus Corwin</div>
      <div class="person-title">Managing Director</div>
    </div>

    <div class="back-brand">
      <span class="brand-square"></span>
      <span class="brand-name">Corwin Crest Homes</span>
    </div>

    <div class="divider"></div>

    <div class="company">
      <div class="company-name">Corwin Crest Homes, LLC</div>
      <div class="contact-line">
        <svg class="icon" viewBox="0 0 20 20"><circle cx="10" cy="10" r="8" fill="none" stroke="var(--brand-blue)" stroke-width="2"/><path d="M2 10h16M10 2c3 3 3 13 0 16M10 2c-3 3-3 13 0 16" fill="none" stroke="var(--brand-blue)" stroke-width="1.5"/></svg>
        <span>www.corwincresthomes.example</span>
      </div>
    </div>

    <div class="contacts">
      <div class="contact-line">
        <svg class="icon" viewBox="0 0 20 20"><path d="M5 2l3 4-2 2c1 2 3 4 6 6l2-2 4 3-2 3C9 18 2 11 2 4z" fill="var(--brand-blue)"/></svg>
        <span>(555) 017-2846</span>
      </div>
      <div class="contact-line">
        <svg class="icon" viewBox="0 0 20 20"><rect x="1" y="4" width="18" height="12" fill="var(--brand-blue)"/><path d="M1 4l9 7 9-7" fill="none" stroke="#fff" stroke-width="1.5"/></svg>
        <span>corwincresthomes@mailnest.example</span>
      </div>
    </div>

    <div class="license">License: CORWICH462KX</div>
  </section>

</main>
</body>
</html>
```